Turn this into a clear and concise

Attached is a screen shot that we currently show to investors from a software program. We need you to illustrate this in a much more professional looking and easy to view and understand way. If we like your style and attention to detail there is more work behind this.
Industry/Entity Type
Software

```html
<!DOCTYPE html>
<html lang="en">
<head>
<meta charset="utf-8">
<title>Intraday Price, Momentum and Volume</title>
<link rel="stylesheet" href="https://fonts.googleapis.com/css2?family=Lato:wght@400&display=swap">
<style>
  :root {
    --bg: #4f6166;
    --session: #67777e;
    --grid: #b9c5cd;
    --divider: #8795a0;
    --label: #ffffff;
    --up: #5bb52d;
    --down: #f20a0a;
    --wick: #000000;
    --osc: #64bc2e;
    --overbought: #f58a12;
    --oversold: #9a5bb6;
    --volume: #3f8fcb;
  }
  html, body { margin: 0; padding: 0; width: 960px; height: 1200px; overflow: hidden; background: var(--bg); }
  .chart { display: block; width: 960px; height: 1200px; }
  .axis-label { font-family: "Lato", sans-serif; font-size: 44px; fill: var(--label); }
  .grid line { stroke: var(--grid); stroke-width: 3; }
  .divider { stroke: var(--divider); stroke-width: 3; }
  .wicks path { stroke: var(--wick); stroke-width: 3; fill: none; }
  .candle-up { fill: var(--up); }
  .candle-down { fill: var(--down); }
  .doji { stroke: var(--wick); stroke-width: 3; }
  .osc-line { fill: none; stroke: var(--osc); stroke-width: 5; stroke-linejoin: round; }
  .level-high { stroke: var(--overbought); stroke-width: 3; }
  .level-low { stroke: var(--oversold); stroke-width: 3; }
  .volume rect { fill: var(--volume); }
</style>
</head>
<body>
<svg class="chart" viewBox="0 0 1200 1500" xmlns="http://www.w3.org/2000/svg" role="img" aria-label="Intraday futures chart with price candles, momentum oscillator and volume">
  <rect width="1200" height="1500" fill="var(--bg)"/>
  <!-- Price panel -->
  <rect class="session" x="312" y="0" width="576" height="537" fill="var(--session)"/>
  <g class="grid">
    <line x1="243" y1="0" x2="243" y2="1422"/>
    <line x1="485" y1="0" x2="485" y2="1422"/>
    <line x1="724" y1="0" x2="724" y2="1422"/>
    <line x1="966" y1="0" x2="966" y2="1422"/>
    <line x1="95" y1="97" x2="1022" y2="97"/>
    <line x1="95" y1="285" x2="1022" y2="285"/>
    <line x1="95" y1="470" x2="1022" y2="470"/>
    <line x1="95" y1="578" x2="1022" y2="578"/>
    <line x1="95" y1="1037" x2="1022" y2="1037"/>
    <line x1="95" y1="1155" x2="1022" y2="1155"/>
    <line x1="95" y1="1290" x2="1022" y2="1290"/>
  </g>
  <line class="divider" x1="0" y1="538" x2="1200" y2="538"/>
  <line class="divider" x1="0" y1="1120" x2="1200" y2="1120"/>

  <g class="wicks">
    <path d="M141 22V85M162 68V115M203 82V98M243 52V71M262 52V84M283 82V115M302 82V115M322 82V148M343 112V222M362 190V240M383 240V410M404 332V440M424 378V503M444 330V410M465 316V350M484 315V333M504 298V333M525 268V315M544 252V305M564 285V315M584 300V333M604 285V333M625 270V318M645 250V305M664 176V317M685 157V222M706 176V222M725 176V240M746 222V317M767 222V285M786 222V270M806 222V270M827 190V255M847 157V240M868 128V192M888 128V176M907 145V176M928 128V176M948 98V160M967 68V118M987 52V88"/>
  </g>
  <g class="candles">
    <rect class="candle-up" x="115" y="5" width="12" height="20"/>
    <rect class="candle-down" x="135" y="22" width="12" height="48"/>
    <rect class="candle-down" x="156" y="68" width="12" height="16"/>
    <rect class="candle-up" x="217" y="68" width="12" height="16"/>
    <rect class="candle-down" x="256" y="68" width="12" height="16"/>
    <rect class="candle-down" x="316" y="112" width="12" height="18"/>
    <rect class="candle-down" x="337" y="128" width="12" height="79"/>
    <rect class="candle-down" x="356" y="207" width="12" height="15"/>
    <rect class="candle-down" x="377" y="240" width="12" height="93"/>
    <rect class="candle-down" x="398" y="345" width="12" height="50"/>
    <rect class="candle-up" x="438" y="330" width="12" height="65"/>
    <rect class="candle-up" x="478" y="315" width="12" height="18"/>
    <rect class="candle-up" x="498" y="315" width="12" height="18"/>
    <rect class="candle-up" x="519" y="285" width="12" height="30"/>
    <rect class="candle-down" x="558" y="285" width="12" height="30"/>
    <rect class="candle-up" x="598" y="298" width="12" height="18"/>
    <rect class="candle-up" x="619" y="270" width="12" height="30"/>
    <rect class="candle-up" x="658" y="190" width="12" height="80"/>
    <rect class="candle-up" x="679" y="176" width="12" height="31"/>
    <rect class="candle-down" x="700" y="176" width="12" height="16"/>
    <rect class="candle-down" x="719" y="176" width="12" height="64"/>
    <rect class="candle-down" x="740" y="240" width="12" height="30"/>
    <rect class="candle-up" x="761" y="222" width="12" height="48"/>
    <rect class="candle-up" x="821" y="207" width="12" height="33"/>
    <rect class="candle-up" x="841" y="176" width="12" height="46"/>
    <rect class="candle-up" x="862" y="128" width="12" height="48"/>
    <rect class="candle-down" x="882" y="128" width="12" height="48"/>
    <rect class="candle-up" x="901" y="160" width="12" height="16"/>
    <rect class="candle-up" x="942" y="115" width="12" height="45"/>
    <rect class="candle-up" x="961" y="68" width="12" height="30"/>
  </g>
  <g class="doji">
    <line x1="176" y1="82" x2="190" y2="82"/>
    <line x1="196" y1="82" x2="210" y2="82"/>
    <line x1="236" y1="69" x2="250" y2="69"/>
    <line x1="276" y1="98" x2="290" y2="98"/>
    <line x1="295" y1="98" x2="309" y2="98"/>
    <line x1="417" y1="395" x2="431" y2="395"/>
    <line x1="458" y1="332" x2="472" y2="332"/>
    <line x1="537" y1="285" x2="551" y2="285"/>
    <line x1="577" y1="316" x2="591" y2="316"/>
    <line x1="638" y1="270" x2="652" y2="270"/>
    <line x1="779" y1="240" x2="793" y2="240"/>
    <line x1="799" y1="240" x2="813" y2="240"/>
    <line x1="921" y1="160" x2="935" y2="160"/>
    <line x1="980" y1="68" x2="994" y2="68"/>
  </g>

  <!-- Oscillator panel -->
  <line class="level-high" x1="95" y1="668" x2="1005" y2="668"/>
  <line class="level-low" x1="95" y1="942" x2="1005" y2="942"/>
  <path class="osc-line" d="M123 873 L136 952 Q145 965 165 966 L195 966 Q205 966 208 952 L218 893 Q228 872 245 888 L262 920 Q278 945 290 947 Q308 950 316 966 Q330 995 345 1012 Q352 1018 365 1018 Q380 1024 395 1027 L420 1027 Q430 1027 432 1005 L437 930 Q442 895 455 893 L470 891 Q478 889 485 875 Q495 860 508 857 Q515 854 520 835 L526 800 Q530 790 540 795 Q548 810 556 838 Q565 860 577 858 Q590 855 597 838 L612 785 Q622 745 633 740 L650 738 Q656 735 658 710 L661 668 Q668 648 685 645 Q695 648 705 680 Q714 708 720 770 Q728 820 740 843 Q748 858 752 846 L765 785 Q772 775 780 790 Q790 808 800 805 Q810 800 818 782 Q835 740 852 708 Q862 686 870 672 L880 710 Q888 760 893 765 Q900 758 910 750 L922 748 Q932 745 938 730 L950 685 Q958 660 972 657 L988 658"/>

  <!-- Volume panel -->
  <g class="volume">
    <rect x="117" y="1400" width="8" height="22"/>
    <rect x="137" y="1358" width="8" height="64"/>
    <rect x="158" y="1380" width="8" height="42"/>
    <rect x="179" y="1388" width="8" height="34"/>
    <rect x="199" y="1400" width="8" height="22"/>
    <rect x="219" y="1400" width="8" height="22"/>
    <rect x="239" y="1418" width="8" height="4"/>
    <rect x="258" y="1386" width="8" height="36"/>
    <rect x="279" y="1386" width="8" height="36"/>
    <rect x="298" y="1388" width="8" height="34"/>
    <rect x="318" y="1334" width="8" height="88"/>
    <rect x="339" y="1305" width="8" height="117"/>
    <rect x="358" y="1344" width="8" height="78"/>
    <rect x="379" y="1136" width="8" height="286"/>
    <rect x="400" y="1248" width="8" height="174"/>
    <rect x="420" y="1178" width="8" height="244"/>
    <rect x="440" y="1305" width="8" height="117"/>
    <rect x="461" y="1314" width="8" height="108"/>
    <rect x="480" y="1365" width="8" height="57"/>
    <rect x="500" y="1374" width="8" height="48"/>
    <rect x="521" y="1328" width="8" height="94"/>
    <rect x="540" y="1340" width="8" height="82"/>
    <rect x="560" y="1378" width="8" height="44"/>
    <rect x="580" y="1397" width="8" height="25"/>
    <rect x="600" y="1392" width="8" height="30"/>
    <rect x="621" y="1358" width="8" height="64"/>
    <rect x="641" y="1374" width="8" height="48"/>
    <rect x="660" y="1260" width="8" height="162"/>
    <rect x="681" y="1330" width="8" height="92"/>
    <rect x="702" y="1340" width="8" height="82"/>
    <rect x="721" y="1388" width="8" height="34"/>
    <rect x="742" y="1324" width="8" height="98"/>
    <rect x="763" y="1356" width="8" height="66"/>
    <rect x="782" y="1353" width="8" height="69"/>
    <rect x="802" y="1368" width="8" height="54"/>
    <rect x="823" y="1371" width="8" height="51"/>
    <rect x="843" y="1356" width="8" height="66"/>
    <rect x="864" y="1340" width="8" height="82"/>
    <rect x="884" y="1374" width="8" height="48"/>
    <rect x="903" y="1350" width="8" height="72"/>
    <rect x="924" y="1358" width="8" height="64"/>
    <rect x="944" y="1328" width="8" height="94"/>
    <rect x="963" y="1340" width="8" height="82"/>
    <rect x="983" y="1386" width="8" height="36"/>
  </g>

  <!-- Axis labels -->
  <g class="axis-labels">
    <text class="axis-label" x="1036" y="113">137’08</text>
    <text class="axis-label" x="1036" y="300">136’28</text>
    <text class="axis-label" x="1036" y="485">136’16</text>
    <text class="axis-label" x="1040" y="592">100</text>
    <text class="axis-label" x="1046" y="1053">0</text>
    <text class="axis-label" x="1030" y="1170">20,000</text>
    <text class="axis-label" x="1033" y="1308">10,000</text>
    <text class="axis-label" x="245" y="1480" text-anchor="middle">8am</text>
    <text class="axis-label" x="495" y="1480" text-anchor="middle">9am</text>
    <text class="axis-label" x="739" y="1480" text-anchor="middle">10am</text>
    <text class="axis-label" x="966" y="1480" text-anchor="middle">11am</text>
  </g>
</svg>
</body>
</html>
```